Brenfield Chiropractic Business Cards

[Front]
[KLV/Stormrider LOGO & Brenfield Chiropractic LOGO]
Neck & Back Pain Relief
Dr. Martin Pavely
Doctor of Chiropractic

• Short Term Care For Your Neck & Back Pain
• No Referral Needed
• Affordable / Insurance Accepted
• Proficient in treating Soft Tissue Problems

[Back]
For Valuable Wellness Letter Bulletins™ Emailed To You Free, Go To:
www.DrMartinPavelyJournal.example
[SpinaVault LOGO] - can be small

OFFICE HOURS:
Monday – Thursday
9 am - 12 noon, 2 pm - 6 pm
WALK-INS WELCOME

Industry/Entity Type

Business

Contact Information for Business Card

Brenfield Chiropractic Center, PLLC
4837 Tarrow Avenue, Suite K
Hollisford, NC 28999
(252) 555-0147
www.brenfieldchiro.example

Requirements
Must have
• The KLV/Stormrider Logo
The Brenfield Chiropractic Logo
Should not have
• A picture of a spine

```html
<!DOCTYPE html>
<html lang="en">
<head>
<meta charset="utf-8">
<title>Brenfield Chiropractic Business Cards</title>
<link rel="stylesheet" href="https://fonts.googleapis.com/css2?family=Open+Sans:wght@400;600;700&display=swap">
<style>
  :root {
    --backdrop: #6e6e6e;
    --card: #ffffff;
    --ink: #1a1a1a;
    --brand-blue: #1f5fa8;
    --icon-blue: #1e56a0;
    --deep-violet: #2e2a85;
    --badge-red: #d5232f;
    --badge-navy: #1c3f8c;
    --rule: #222222;
  }
  * { margin: 0; padding: 0; box-sizing: border-box; }
  html, body { width: 1200px; height: 590px; overflow: hidden; }
  body {
    background: var(--backdrop);
    font-family: "Open Sans", Arial, sans-serif;
    color: var(--ink);
    position: relative;
  }
  .card {
    position: absolute;
    top: 140px;
    width: 533px;
    height: 312px;
    background: var(--card);
    overflow: hidden;
  }
  .card--front { left: 35px; }
  .card--back { left: 605px; }
  .abs { position: absolute; }

  /* Front */
  .doctor-name { left: 33px; top: 71px; font-size: 17px; font-weight: 700; color: var(--brand-blue); text-transform: uppercase; letter-spacing: 0.2px; }
  .doctor-name .title-abbr { text-transform: none; }
  .doctor-role { left: 33px; top: 94px; font-size: 13px; }
  .brand-wordmark { left: 248px; top: 60px; font-size: 22px; font-weight: 400; color: var(--ink); font-variant: small-caps; letter-spacing: 1px; white-space: nowrap; display: flex; align-items: center; gap: 8px; }
  .brand-dot { width: 12px; height: 12px; border-radius: 50%; background: var(--deep-violet); display: inline-block; }
  .brand-tagline { left: 248px; top: 122px; font-size: 13px; font-weight: 700; letter-spacing: 3.1px; white-space: nowrap; }
  .contact-list { left: 33px; top: 161px; list-style: none; font-size: 12.5px; line-height: 18.6px; white-space: nowrap; }
  .contact-list li { display: flex; align-items: center; gap: 7px; }
  .contact-icon { width: 12px; height: 12px; flex: none; }
  .address { left: 33px; top: 235px; font-size: 12.5px; line-height: 18.6px; white-space: nowrap; }
  .divider { left: 228px; top: 160px; width: 1.5px; height: 76px; background: var(--rule); }
  .benefits { left: 246px; top: 161px; list-style: none; font-size: 12.5px; line-height: 18.6px; white-space: nowrap; }
  .benefits li::before { content: "• "; }
  .partner-badge { top: 252px; height: 36px; }
  .partner-badge--klv { left: 234px; width: 126px; }
  .partner-badge--stormrider { left: 368px; width: 142px; }

  /* Back */
  .newsletter { left: 29px; top: 26px; font-size: 13px; line-height: 19px; white-space: nowrap; }
  .vault-mark { left: 29px; top: 64px; font-size: 24px; font-weight: 400; color: var(--brand-blue); display: flex; align-items: center; gap: 6px; }
  .vault-square { width: 14px; height: 14px; background: var(--brand-blue); display: inline-block; }
  .appointments { left: 29px; top: 105px; font-size: 13px; line-height: 24px; white-space: nowrap; }
  .appointments .blank { display: inline-block; border-bottom: 1px solid var(--ink); width: 104px; height: 12px; }
  .appointments .blank--time { width: 43px; }
  .office-hours { left: 29px; top: 180px; font-size: 13px; line-height: 18.6px; white-space: nowrap; }
  .office-hours h2 { font-size: 13px; font-weight: 700; }
  .brand-decoration { left: 280px; top: 75px; width: 253px; height: 237px; }
</style>
</head>
<body>

<section class="card card--front" aria-label="Business card front">
  <div class="abs brand-wordmark"><span class="brand-dot"></span>Brenfield Chiropractic</div>
  <div class="abs brand-tagline">NECK &amp; BACK PAIN RELIEF</div>

  <h1 class="abs doctor-name"><span class="title-abbr">Dr.</span> Martin Pavely</h1>
  <p class="abs doctor-role">Doctor of Chiropractic</p>

  <ul class="abs contact-list">
    <li>
      <svg class="contact-icon" viewBox="0 0 12 12"><rect width="12" height="12" rx="2" fill="var(--icon-blue)"/><path d="M3.5 2.6l1.5 0 .6 1.8-.9.7c.4.9 1.1 1.6 2 2l.7-.9 1.8.6v1.5c-3.2.2-5.9-2.5-5.7-5.7z" fill="#fff"/></svg>
      (252) 555-0147
    </li>
    <li>
      <svg class="contact-icon" viewBox="0 0 12 12"><rect width="12" height="12" rx="2" fill="var(--icon-blue)"/><rect x="3.5" y="2.5" width="5" height="2.5" fill="#fff"/><rect x="2.5" y="5" width="7" height="3" fill="#fff"/><rect x="3.8" y="7.2" width="4.4" height="2.3" fill="#fff" stroke="var(--icon-blue)" stroke-width=".6"/></svg>
      (252) 555-0183
    </li>
    <li>
      <svg class="contact-icon" viewBox="0 0 12 12"><rect width="12" height="12" rx="2" fill="var(--icon-blue)"/><rect x="2.5" y="3.5" width="7" height="5" fill="#fff"/><path d="M2.5 3.5l3.5 2.8 3.5-2.8" fill="none" stroke="var(--icon-blue)" stroke-width=".8"/></svg>
      info@brenfield.example
    </li>
    <li>
      <svg class="contact-icon" viewBox="0 0 12 12"><rect width="12" height="12" rx="2" fill="var(--icon-blue)"/><circle cx="6" cy="6" r="3.4" fill="none" stroke="#fff" stroke-width=".8"/><path d="M2.6 6h6.8M6 2.6v6.8" stroke="#fff" stroke-width=".7"/></svg>
      www.brenfieldchiro.example
    </li>
  </ul>
  <p class="abs address">4837 Tarrow Avenue, Suite K<br>Hollisford, NC 28999</p>

  <div class="abs divider"></div>
  <ul class="abs benefits">
    <li>Short Term Care For Your Neck &amp; Back Pain</li>
    <li>No Referral Needed</li>
    <li>Affordable / Insurance Accepted</li>
    <li>Proficient in treating Soft Tissue Problems</li>
  </ul>

  <svg class="abs partner-badge partner-badge--klv" viewBox="0 0 126 36" role="img" aria-label="KLV partner badge">
    <ellipse cx="45" cy="17" rx="44" ry="14" fill="var(--badge-red)"/>
  </svg>
  <svg class="abs partner-badge partner-badge--stormrider" viewBox="0 0 142 36" role="img" aria-label="Stormrider partner badge">
    <rect x="0" y="2" width="2" height="32" fill="var(--badge-navy)"/>
    <rect x="8" y="10" width="132" height="20" fill="var(--badge-navy)"/>
  </svg>
</section>

<section class="card card--back" aria-label="Business card back">
  <p class="abs newsletter">For Valuable Wellness Letter Bulletins™ Emailed To You Free, Go To:<br>www.DrMartinPavelyJournal.example</p>
  <div class="abs vault-mark"><span class="vault-square"></span>SpinaVault</div>

  <div class="abs appointments">
    <p>Date<span class="blank"></span>Time<span class="blank blank--time"></span></p>
    <p>Date<span class="blank"></span>Time<span class="blank blank--time"></span></p>
    <p>Date<span class="blank"></span>Time<span class="blank blank--time"></span></p>
  </div>

  <div class="abs office-hours">
    <h2>OFFICE HOURS:</h2>
    <p>Monday – Thursday:</p>
    <p>9 am - 12 noon</p>
    <p>2 pm - 6 pm</p>
    <p>WALK-INS WELCOME</p>
  </div>

  <svg class="abs brand-decoration" viewBox="0 0 253 237" role="img" aria-label="Large decorative brand symbol area in violet, gold and sky blue">
    <defs>
      <linearGradient id="decorTones" x1="0" y1="0" x2="1" y2="1">
        <stop offset="0" stop-color="#ecebf6"/>
        <stop offset="0.5" stop-color="#e3f3fb"/>
        <stop offset="1" stop-color="#cfeaf7"/>
      </linearGradient>
    </defs>
    <rect width="253" height="237" fill="url(#decorTones)"/>
  </svg>
</section>

</body>
</html>
```